bramblegate crest roofing flyer*

I need an a5 size flyer designing to go in our local advertising magazine.We are based in the north west of England Id like key features from the website including on the flyer, possibly even reviews, what we do ect.I don't however want it too busy, simple pictures and description of service.company colours and logo. I require simple one sided business cards toonumber, web address and logowinner will receive a request to design around 5 different double sided a5 flyers too, each with all our services on one side and the other primarily for one service we have provided locally with a spacve to put the house number down.REPAIRSROOFLINEFLAT ROOFS PITCHED ROOFSSYNTHETIC ROOFSUP TO 50 YEARS WARRANTY AVAILABLERANKED THE #1 FLAT ROOFER IN THE UK OUT OF 787 REGISTERED FLAT ROOFING COMPANIESRANKED THE #10 ROOFING COMPANY IN THE UK OUT OF 1976 REGISTERED SPECIALIST ROOFING COMPANIESBOTH FOR COST, CUSTOMER SERVICE AND QUALITY WITH 5 STAR REVIEWSGUARANTEED TO FIND AND FIX A LEAKAPPROVED INSTALLERSAWARD WINNINGTIME SERVED FIXED PRICES

Target Market(s)

homeowners

Colors

Designer to choose only greyscale colors for use in the design.

Requirements
Must have
• contact details
• pictures of my work
• clear and simple

```html
<!DOCTYPE html>
<html lang="en">
<head>
<meta charset="utf-8">
<title>Bramblegate Crest Roofing – A5 Flyer</title>
<link rel="stylesheet" href="https://fonts.googleapis.com/css2?family=Montserrat:wght@500;600;800&family=Oswald:wght@500&display=swap">
<style>
  :root {
    --green: #3f8f37;
    --green-dark: #2f7a2a;
    --yellow: #f2c200;
    --white: #ffffff;
    --ink: #1b1b1b;
    --backdrop: #5d5e72;
  }
  * { box-sizing: border-box; margin: 0; padding: 0; }
  html, body { width: 1200px; height: 800px; overflow: hidden; }
  body { background: var(--backdrop); position: relative; font-family: "Montserrat", sans-serif; }

  .flyer {
    position: absolute; left: 320px; top: 10px;
    width: 560px; height: 780px;
    background: var(--green); overflow: hidden;
  }
  .flyer__frame { position: absolute; inset: 0; }

  .brand {
    position: absolute; left: 38px; top: 110px; width: 270px;
    color: var(--white); font-weight: 800; line-height: 1.02;
    text-transform: uppercase; letter-spacing: 1px;
  }
  .brand__line--top { font-size: 30px; }
  .brand__line--bottom { font-size: 44px; letter-spacing: 4px; }

  .quote-band {
    position: absolute; left: 0; top: 250px; width: 345px; height: 52px;
    background: var(--yellow); border-radius: 0 40px 0 0;
    font-family: "Oswald", sans-serif; font-weight: 500; font-size: 27px;
    color: var(--ink); padding: 8px 0 0 26px;
  }

  .services-tab {
    position: absolute; left: 0; top: 572px; width: 300px; height: 56px;
    background: var(--yellow); border-radius: 0 0 60px 0;
    font-weight: 600; font-size: 30px; color: var(--ink); padding: 7px 0 0 28px;
  }

  .service-list {
    position: absolute; left: 24px; top: 638px; list-style: none;
  }
  .service-list__item {
    display: flex; align-items: center; gap: 26px;
    color: var(--white); font-size: 20px; font-weight: 500; height: 28px; margin-bottom: 2px;
  }
  .service-list__icon { width: 26px; height: 26px; flex: none; }

  .recommend {
    position: absolute; left: 372px; top: 586px; width: 180px; text-align: center;
  }
  .recommend__seal { width: 100px; height: 100px; display: block; margin: 0 auto; }
  .recommend__text { color: var(--white); font-size: 12.5px; line-height: 1.3; margin-top: 4px; }

  .contact-bar {
    position: absolute; left: 0; bottom: 0; width: 560px; height: 46px;
    background: var(--yellow); display: flex; align-items: center;
    font-family: "Oswald", sans-serif; color: var(--ink);
  }
  .contact-bar__web { display: flex; align-items: center; gap: 12px; padding-left: 20px; width: 320px; font-size: 15px; }
  .contact-bar__rule { width: 2px; height: 26px; background: var(--ink); }
  .contact-bar__phone { display: flex; align-items: center; gap: 14px; padding-left: 30px; font-size: 25px; }
  .contact-bar__icon { width: 26px; height: 26px; flex: none; }
</style>
</head>
<body>
  <article class="flyer">
    <svg class="flyer__frame" width="560" height="780" viewBox="0 0 560 780">
      <polyline points="0,38 400,38 460,10 560,60" fill="none" stroke="var(--white)" stroke-width="4"/>
      <polyline points="0,48 404,48 460,22 560,72" fill="none" stroke="var(--yellow)" stroke-width="9"/>
      <polygon points="300,220 400,110 460,78 560,128 560,330 340,330" fill="var(--white)"/>
      <defs>
        <linearGradient id="houseTones" x1="0" y1="0" x2="0" y2="1">
          <stop offset="0" stop-color="#a9cdea"/>
          <stop offset="0.45" stop-color="#a33a2e"/>
          <stop offset="0.8" stop-color="#5a8d3a"/>
          <stop offset="1" stop-color="#6c9a3f"/>
        </linearGradient>
        <linearGradient id="aerialTones" x1="0" y1="0" x2="1" y2="1">
          <stop offset="0" stop-color="#4f8a36"/>
          <stop offset="0.5" stop-color="#8a8592"/>
          <stop offset="1" stop-color="#3d6f2c"/>
        </linearGradient>
        <linearGradient id="terraceTones" x1="0" y1="0" x2="0" y2="1">
          <stop offset="0" stop-color="#4f8fd6"/>
          <stop offset="0.45" stop-color="#3e4250"/>
          <stop offset="1" stop-color="#8b8472"/>
        </linearGradient>
      </defs>
      <polygon role="img" aria-label="Photo of a red timber house with a new tiled roof" points="308,220 404,116 460,86 552,132 552,322 344,322" fill="url(#houseTones)"/>
      <rect x="0" y="312" width="560" height="254" fill="var(--white)"/>
      <polygon role="img" aria-label="Aerial photo of a large house with a finished shingle roof" points="0,322 300,322 290,556 0,556" fill="url(#aerialTones)"/>
      <polygon role="img" aria-label="Photo of a terrace of houses with new pitched roofs" points="310,322 560,322 560,556 300,556" fill="url(#terraceTones)"/>
      <rect x="0" y="560" width="560" height="8" fill="var(--yellow)"/>
      <polygon points="360,596 366,596 352,734 346,734" fill="var(--yellow)"/>
    </svg>

    <h1 class="brand">
      <span class="brand__line--top">Bramblegate Crest</span><br>
      <span class="brand__line--bottom">Roofing</span>
    </h1>

    <p class="quote-band">Get a Fixed Priced Quote</p>

    <h2 class="services-tab">Our Services.</h2>

    <ul class="service-list">
      <li class="service-list__item">
        <svg class="service-list__icon" viewBox="0 0 26 26"><circle cx="13" cy="13" r="12" fill="none" stroke="var(--yellow)" stroke-width="1.6"/><polyline points="6,15 13,8 20,15" fill="none" stroke="var(--yellow)" stroke-width="1.6"/></svg>
        Flat Roofing
      </li>
      <li class="service-list__item">
        <svg class="service-list__icon" viewBox="0 0 26 26"><circle cx="13" cy="13" r="12" fill="none" stroke="var(--yellow)" stroke-width="1.6"/><path d="M7 18V10M11 18V9M15 18V9M19 18V10M6 13H20" fill="none" stroke="var(--yellow)" stroke-width="1.4"/></svg>
        Pitched Roofing
      </li>
      <li class="service-list__item">
        <svg class="service-list__icon" viewBox="0 0 26 26"><circle cx="13" cy="13" r="12" fill="none" stroke="var(--yellow)" stroke-width="1.6"/><path d="M8 18L16 10M15 8L18 11" fill="none" stroke="var(--yellow)" stroke-width="1.8"/></svg>
        Repairs &amp; Roof line
      </li>
    </ul>

    <aside class="recommend">
      <svg class="recommend__seal" viewBox="0 0 118 118" role="img" aria-label="Certificate of excellence badge">
        <circle cx="59" cy="59" r="56" fill="none" stroke="var(--yellow)" stroke-width="3"/>
        <circle cx="59" cy="59" r="46" fill="var(--yellow)"/>
        <rect x="13" y="50" width="92" height="18" fill="var(--white)"/>
      </svg>
      <p class="recommend__text">Highly Recommended by<br>Nearlist Users</p>
    </aside>

    <footer class="contact-bar">
      <div class="contact-bar__web">
        <svg class="contact-bar__icon" viewBox="0 0 26 26"><circle cx="13" cy="13" r="12" fill="var(--ink)"/><circle cx="13" cy="13" r="6.5" fill="none" stroke="var(--white)" stroke-width="1.3"/><path d="M6.5 13H19.5M13 6.5C10 10 10 16 13 19.5M13 6.5C16 10 16 16 13 19.5" fill="none" stroke="var(--white)" stroke-width="1.1"/></svg>
        www.bramblegatecrestroofing.com
      </div>
      <span class="contact-bar__rule"></span>
      <div class="contact-bar__phone">
        <svg class="contact-bar__icon" viewBox="0 0 26 26"><circle cx="13" cy="13" r="12" fill="var(--ink)"/><path d="M9 7.5C8 9 8.5 13 11 15.5S17 19 18.5 18L16.5 15.5L14.8 16.3C13.5 15.5 11.5 13.5 10.7 12.2L11.5 10.5Z" fill="var(--white)"/></svg>
        07700900418
      </div>
    </footer>
  </article>
</body>
</html>
```